Professional Report Cover

We need a cover for CFO report (the document is about 20 pages, in case you decide to provide 3D mockup). The design must be professional. The main color has to be #299FC0, which can be incorporated with white, #375172, and #E3E7EE. See attached for content and logo.

```html
<!DOCTYPE html>
<html lang="en">
<head>
<meta charset="utf-8">
<title>The CFO Insight — Report Cover</title>
<link rel="stylesheet" href="https://fonts.googleapis.com/css2?family=Montserrat:wght@500;600;700;800&display=swap">
<style>
  :root {
    --teal: #299FC0;
    --navy: #375172;
    --mist: #E3E7EE;
    --white: #FFFFFF;
    --stage: #D8D9DB;
    --band-deep: #0B1A3A;
    --band-mid: #12307A;
    --band-glow: #2F6FE0;
  }
  * { margin: 0; padding: 0; box-sizing: border-box; }
  html, body {
    width: 1200px;
    height: 853px;
    overflow: hidden;
    background: var(--stage);
    font-family: "Montserrat", sans-serif;
  }
  .cover {
    position: absolute;
    left: 305px;
    top: 36px;
    width: 590px;
    height: 780px;
    background: var(--mist);
    overflow: hidden;
    box-shadow: 0 10px 30px rgba(0,0,0,0.12);
  }
  .cover__accent {
    position: absolute;
    left: 0;
    top: 0;
    width: 180px;
    height: 8px;
    background: var(--teal);
  }
  .cover__title {
    position: absolute;
    left: 0;
    right: 0;
    top: 48px;
    text-align: center;
    font-weight: 800;
    line-height: 0.88;
    z-index: 3;
  }
  .cover__title span { display: block; }
  .title__the { color: var(--navy); font-size: 120px; letter-spacing: -1px; }
  .title__cfo { color: var(--teal); font-size: 120px; letter-spacing: -1px; }
  .title__insight { color: var(--navy); font-size: 120px; letter-spacing: -2px; }

  .feature-band {
    position: absolute;
    left: 0;
    right: 0;
    top: 345px;
    height: 340px;
    border-bottom: 9px solid var(--teal);
  }
  .feature-band__visual {
    position: absolute;
    inset: 0;
    background:
      radial-gradient(circle at 30% 50%, var(--band-glow) 0%, var(--band-mid) 30%, transparent 62%),
      linear-gradient(90deg, var(--band-mid) 0%, var(--band-deep) 55%, #0E1E2E 100%);
  }
  .includes-tab {
    position: absolute;
    right: 0;
    top: 360px;
    width: 250px;
    height: 28px;
    background: var(--teal);
    color: var(--white);
    font-weight: 600;
    font-size: 15px;
    letter-spacing: 9px;
    line-height: 28px;
    padding-left: 18px;
    z-index: 4;
  }
  .includes-list {
    position: absolute;
    left: 345px;
    right: 22px;
    top: 404px;
    list-style: none;
    color: var(--white);
    font-size: 13.5px;
    font-weight: 500;
    line-height: 1.3;
    z-index: 4;
  }
  .includes-list li { margin-bottom: 13px; }
  .includes-list li:last-child { margin-bottom: 0; }

  .brand {
    position: absolute;
    left: 0;
    right: 0;
    top: 712px;
    text-align: center;
  }
  .brand__name {
    display: inline-flex;
    align-items: center;
    gap: 8px;
    font-size: 17px;
    font-weight: 700;
    color: var(--navy);
  }
  .brand__mark {
    width: 12px;
    height: 12px;
    background: var(--navy);
  }
  .brand__tagline {
    margin-top: 8px;
    font-size: 7.5px;
    font-weight: 600;
    letter-spacing: 1.5px;
    color: var(--navy);
    text-transform: uppercase;
  }
</style>
</head>
<body>
  <main class="cover">
    <div class="cover__accent"></div>

    <h1 class="cover__title">
      <span class="title__the">The</span>
      <span class="title__cfo">CFO</span>
      <span class="title__insight">Insight</span>
    </h1>

    <section class="feature-band">
      <div class="feature-band__visual" role="img" aria-label="Photo of a business executive in a suit holding a glowing digital CFO target icon surrounded by circular tech icons"></div>
    </section>

    <div class="includes-tab">INCLUDES</div>

    <ul class="includes-list">
      <li>Insight into external, enterprise and departmental challenges</li>
      <li>Best practices and strategies to solve these challenges, with a focus on innovation, securing competitive advantage and opportunities for growth</li>
      <li>Finance industry trends in the 2020s</li>
      <li>The leading role of CFOs in business transformation</li>
    </ul>

    <footer class="brand">
      <div class="brand__name"><span class="brand__mark"></span>Northvale Document Group</div>
      <div class="brand__tagline">A Meridian Group Company</div>
    </footer>
  </main>
</body>
</html>
```